Online trading school - Website design

We are building an online trading school (trading of shares, commodities, indices, currencies). The purpose is to teach online traders how to trade successfully. We need to design the homepage of the website and logo (bramwelloq.com will be the domain). The homepage will contain the following elements

- logo
- Sign in and Register links/buttons
- upper menu
- short introduction
- a couple of bullet points 'Why to join our school?'
- sign up form
- text
- bottom menu

Attached is a draft for the designer. The draft is just for an inspiration, the actual structure of the website can be different if the designer thinks so.

The designer is free to choose colors.

School

3 page

```html
<!DOCTYPE html>
<html lang="en">
<head>
<meta charset="utf-8">
<title>Bramwelloq – Online training for trading</title>
<link href="https://fonts.googleapis.com/css2?family=Lato:wght@400;700&family=Raleway:wght@500;600;700&display=swap" rel="stylesheet">
<style>
:root{
  --orange:#f58220;
  --blue:#0f6db0;
  --navy:#0a5a96;
  --dark:#23272f;
  --darker:#1a1d23;
  --text:#333;
  --muted:#555;
  --light:#ececec;
  --white:#fff;
}
*{margin:0;padding:0;box-sizing:border-box}
html,body{width:978px;height:1200px;overflow:hidden;background:var(--white)}
body{position:relative;font-family:'Lato',sans-serif;color:var(--text)}
.abs{position:absolute}

/* header */
.site-header{left:0;top:0;width:978px;height:74px;background:linear-gradient(#fff,#f3f3f3);border-bottom:1px solid var(--blue)}
.brand{left:132px;top:10px;display:flex;align-items:center;gap:10px}
.brand-mark{width:46px;height:46px;border-radius:50%;background:var(--blue)}
.brand-name{font-family:'Raleway',sans-serif;font-weight:700;font-size:21px;color:var(--blue);line-height:1}
.brand-tag{font-size:10px;font-weight:700;color:var(--text);margin-top:3px;letter-spacing:.4px}
.social-top{left:613px;top:14px;display:flex;gap:4px}
.social-top span{width:19px;height:19px;background:#8a96a8;border-radius:2px}
.btn-auth{top:10px;height:26px;color:#fff;font-family:'Raleway',sans-serif;font-weight:700;font-size:9px;display:flex;align-items:center;justify-content:center}
.btn-login{left:696px;width:68px;background:var(--orange)}
.btn-register{left:769px;width:77px;background:var(--blue)}
.main-nav{right:132px;top:49px;display:flex;gap:17px;font-family:'Raleway',sans-serif;font-size:10px;font-weight:500}
.main-nav a{color:var(--text);text-decoration:none}
.main-nav a.active{color:var(--blue);font-weight:700}

/* hero */
.hero-photo{left:0;top:75px;width:978px;height:281px;background:linear-gradient(90deg,#8a7a6e 0%,#c9d8e4 30%,#e8f0f6 55%,#bfcfdc 75%,#8f7e72 100%)}
.hero-band{left:0;top:356px;width:978px;height:35px;background:var(--orange);color:#fff;font-family:'Raleway',sans-serif;font-weight:700;font-size:17px;display:flex;align-items:center;justify-content:center}

/* why */
.why{left:0;top:391px;width:978px;height:284px;background:linear-gradient(90deg,#dcdcdc,#efefef 40%,#e4e4e4 70%,#d6d6d6)}
.section-title{font-family:'Raleway',sans-serif;font-weight:700}
.why-title{left:132px;top:426px;font-size:20px;color:var(--orange)}
.why-title b,.offer-title b{color:var(--blue)}
.why-rule{left:132px;top:460px;width:86px;height:1px;background:#aaa}
.why-rule::before{content:"";position:absolute;left:0;top:-1px;width:26px;height:2px;background:#444}
.why-item{display:flex;align-items:center;gap:9px;font-size:12px;font-weight:700;color:var(--text)}
.why-icon{width:41px;height:41px;border-radius:50%;border:3px solid var(--orange);border-top-color:var(--blue);border-left-color:var(--blue);background:#fff;display:flex;align-items:center;justify-content:center}
.why-divider{left:569px;top:460px;width:1px;height:160px;background:#b9b9b9}

/* signup */
.signup{left:621px;top:428px;width:225px;height:210px;background:#f1f1f1;box-shadow:0 6px 10px rgba(0,0,0,.18)}
.signup-head{height:35px;background:linear-gradient(var(--blue),var(--navy));color:#fff;font-family:'Raleway',sans-serif;font-weight:700;font-size:14.5px;display:flex;align-items:center;justify-content:center}
.field{position:absolute;left:12px;width:202px;height:28px;background:#fff;border:1px solid #ddd;font-size:9px;color:#444;padding:0 8px;display:flex;align-items:center}
.agree{position:absolute;left:14px;top:152px;font-size:8.5px;color:#444;display:flex;align-items:center;gap:7px}
.agree i{width:8px;height:8px;border:1px solid #aaa;background:#fff}
.signup-submit{position:absolute;left:12px;top:171px;width:202px;height:28px;background:var(--blue);color:#fff;font-family:'Raleway',sans-serif;font-weight:700;font-size:12px;display:flex;align-items:center;justify-content:center}

/* offer */
.offer-title{left:0;top:708px;width:978px;text-align:center;font-size:21px;color:var(--orange)}
.offer-rule{left:433px;top:742px;width:112px;height:1px;background:#bbb}
.offer-rule::before{content:"";position:absolute;left:43px;top:-1px;width:26px;height:2px;background:#444}
.offer-text{left:140px;top:758px;width:698px;text-align:center;font-size:11.4px;line-height:22px;color:#444}

/* footer */
.swoosh{left:0;top:830px}
.footer{left:0;top:969px;width:978px;height:198px;background:var(--dark)}
.foot-head{font-family:'Raleway',sans-serif;font-weight:700;font-size:12.5px;color:var(--orange);padding-bottom:6px;border-bottom:1px solid #555}
.quick{left:132px;top:995px;width:140px}
.quick ul{list-style:none;margin-top:6px}
.quick li{font-family:'Raleway',sans-serif;font-size:10px;color:#ddd;height:27px;display:flex;align-items:center;gap:6px}
.quick li::before{content:"";width:3px;height:3px;background:#777}
.quick li.active{color:var(--orange)}
.news{left:311px;top:995px;width:170px}
.news p{font-size:8.6px;line-height:13px;color:#ddd;margin-top:8px}
.news p b{color:#fff}
.news-input{position:absolute;left:-1px;top:84px;width:170px;height:27px;background:#fff;border-radius:2px;font-size:9.5px;color:#666;padding-left:8px;display:flex;align-items:center}
.news-submit{position:absolute;left:-1px;top:122px;width:79px;height:26px;background:var(--orange);color:#fff;font-family:'Raleway',sans-serif;font-weight:700;font-size:11.5px;display:flex;align-items:center;justify-content:center;box-shadow:0 2px 0 #000}
.contact{left:521px;top:995px;width:325px}
.contact h4{font-family:'Raleway',sans-serif;font-weight:700;font-size:11.5px;color:#eee;margin-top:9px}
.contact p{font-size:9.5px;line-height:14px;color:#ccc;width:125px}
.contact-line{display:flex;align-items:center;gap:7px;font-size:10px;color:#ccc;position:absolute;left:0}
.map{left:665px;top:1025px;width:181px;height:118px;background:linear-gradient(135deg,#cfe0c9,#e9ecd6 50%,#a9c9e6);border:1px solid #999}
.bottom-bar{left:0;top:1167px;width:978px;height:33px;background:var(--darker)}
.copyright{left:132px;top:1179px;font-family:'Raleway',sans-serif;font-size:10px;color:#ccc}
.copyright b{color:#fff}
.social-bottom{left:773px;top:1174px;display:flex;gap:5px}
.social-bottom span{width:21px;height:21px;border-radius:50%;background:#c9c9c9}
</style>
</head>
<body>

<header class="abs site-header">
  <div class="abs brand">
    <div class="brand-mark"></div>
    <div>
      <div class="brand-name">BRAMWELLOQ</div>
      <div class="brand-tag">Online training for trading</div>
    </div>
  </div>
  <div class="abs social-top" aria-label="Social links"><span></span><span></span><span></span></div>
  <div class="abs btn-auth btn-login">LOGIN</div>
  <div class="abs btn-auth btn-register">REGISTER</div>
  <nav class="abs main-nav">
    <a class="active">HOME</a><a>ABOUT OUR SCHOOL</a><a>RISK WARNING</a><a>FAQ</a><a>TRADING GLOSSARY</a><a>CONTACT US</a>
  </nav>
</header>

<div class="abs hero-photo" role="img" aria-label="Photo of a trainer presenting a chart on a flipchart to a seated audience in a bright office"></div>
<div class="abs hero-band">Trade From The Comfort Of your&nbsp; Place</div>

<section class="abs why" role="img" aria-label="Faded background photo of a classroom presentation"></section>
<h2 class="abs section-title why-title">WHY TO <b>JOIN US?</b></h2>
<div class="abs why-rule"></div>
<div class="abs why-item" style="left:132px;top:475px"><div class="why-icon"></div>Best trading tips ever</div>
<div class="abs why-item" style="left:358px;top:475px"><div class="why-icon"></div>Best trading tips ever</div>
<div class="abs why-item" style="left:132px;top:536px"><div class="why-icon"></div>Best trading tips ever</div>
<div class="abs why-item" style="left:358px;top:536px"><div class="why-icon"></div>Best trading tips ever</div>
<div class="abs why-item" style="left:255px;top:598px"><div class="why-icon"></div>Best trading tips ever</div>
<div class="abs why-divider"></div>

<form class="abs signup">
  <div class="signup-head">JOIN OUR SCHOOL NOW</div>
  <div class="field" style="top:49px">First Name</div>
  <div class="field" style="top:83px">Last Name</div>
  <div class="field" style="top:116px">Email</div>
  <div class="agree"><i></i>Agree with our terms and conditions</div>
  <div class="signup-submit">SUBMIT</div>
</form>

<h2 class="abs section-title offer-title">What Do <b>We Offer ?</b></h2>
<div class="abs offer-rule"></div>
<p class="abs offer-text">Lorem ipsum dolor sit amet, consectetuer adipiscing elit, sed diam nonummy nibh euismod tincidunt ut laoreet dolore magna aliquam erat volutpat. Ut wisi enim ad minim veniam, quis nostrud exerci tation ullamcorper suscipit lobortis nisl ut aliquip ex ea commodo consequat. Duis autem vel eum iriure dolor in hendrerit in vulputate velit esse molestie consequat, vel illum dolore eu feugiat nulla facilisis at vero eros et accumsan et iusto odio dignissim qui blandit praesent luptatum zzril delenit augue duis dolore te feugait nulla facilisis.</p>

<svg class="abs swoosh" width="978" height="140" viewBox="0 0 978 140">
  <path d="M0,72 C200,125 420,140 560,136 C740,130 890,85 978,45 L978,140 L0,140Z" fill="#23272f"/>
  <path d="M0,4 C90,70 300,124 565,128 C330,134 110,110 0,52Z" fill="#f58220"/>
</svg>
<footer class="abs footer"></footer>

<div class="abs quick">
  <div class="foot-head">QUICK LINKS</div>
  <ul><li class="active">HOME</li><li>ABOUT OUR SCHOOL</li><li>RISK WARNING</li><li>TRADING GLOSSARY</li><li>CONTACT US</li></ul>
</div>

<div class="abs news">
  <div class="foot-head">NEWSLETTER SIGNUP</div>
  <p>Sign up to receive occasional e-mail updates about new features and special offers from <b>Scared!</b></p>
  <div class="news-input">Enter your email here</div>
  <div class="news-submit">SUBMIT</div>
</div>

<div class="abs contact">
  <div class="foot-head">CONTACT INFORMATION</div>
  <h4>BRAMWELLOQ</h4>
  <p>Lorem ipsum dolor sit amet, consectetuer adipiscing elit,Lorem ipsum dolor sit amet, consectetuer .</p>
  <div class="contact-line" style="top:108px">
    <svg width="10" height="10" viewBox="0 0 24 24"><path fill="#ccc" d="M6.6 10.8a15 15 0 006.6 6.6l2.2-2.2c.3-.3.7-.4 1-.2 1.1.4 2.3.6 3.6.6.6 0 1 .4 1 1V20c0 .6-.4 1-1 1A17 17 0 013 4c0-.6.4-1 1-1h3.5c.6 0 1 .4 1 1 0 1.3.2 2.5.6 3.6.1.3 0 .7-.2 1z"/></svg>123 456 7890</div>
  <div class="contact-line" style="top:136px">
    <svg width="11" height="8" viewBox="0 0 22 16"><rect width="22" height="16" fill="#ccc"/><path d="M0,0 L11,9 L22,0" fill="none" stroke="#23272f" stroke-width="2"/></svg>info@bramwelloq.com</div>
</div>
<div class="abs map" role="img" aria-label="Street map showing the school location"></div>

<div class="abs bottom-bar"></div>
<div class="abs copyright">Copyright © 2016 <b>BRAMWELLOQ.</b> All Right Reserved.</div>
<div class="abs social-bottom" aria-label="Social links"><span></span><span></span><span></span></div>

</body>
</html>
```